Criação de Papelaria Profissional para Vértice & Prisma
A empresa queria:
" Desenvolve, vende, implanta o Software e da suporte (Atendimento ao cliente). "

```html
<!DOCTYPE html>
<html lang="pt-BR">
<head>
<meta charset="UTF-8">
<title>Vértice &amp; Prisma — Cartão de visita</title>
<link href="https://fonts.googleapis.com/css2?family=Montserrat:wght@500;600&family=Open+Sans:wght@400;600&display=swap" rel="stylesheet">
<style>
  :root {
    --backdrop: #c9c9c9;
    --card-white: #ffffff;
    --card-black: #1c1c1c;
    --brand-orange: #f08a24;
    --text-dark: #3a3a3a;
  }
  * { margin: 0; padding: 0; box-sizing: border-box; }
  html, body {
    width: 1200px;
    height: 1200px;
    overflow: hidden;
    background: var(--backdrop);
  }
  .business-card {
    position: absolute;
    left: 43px;
    top: 449px;
    width: 1116px;
    height: 302px;
    background: var(--card-white);
    box-shadow: 0 4px 12px rgba(0,0,0,0.25);
    overflow: hidden;
  }
  .card-panels {
    position: absolute;
    inset: 0;
  }
  .contact-side {
    position: absolute;
    left: 72px;
    top: 0;
    font-family: "Open Sans", sans-serif;
  }
  .holder-block {
    position: absolute;
    top: 44px;
    left: 0;
    padding-left: 14px;
    border-left: 4px solid var(--brand-orange);
    white-space: nowrap;
  }
  .holder-name {
    font-family: "Open Sans", sans-serif;
    font-weight: 400;
    font-size: 30px;
    line-height: 36px;
    color: var(--brand-orange);
    text-transform: uppercase;
  }
  .holder-role {
    font-size: 23px;
    line-height: 30px;
    color: var(--text-dark);
  }
  .contact-list {
    position: absolute;
    top: 140px;
    left: 0;
    list-style: none;
  }
  .contact-item {
    display: flex;
    align-items: center;
    height: 36px;
    margin-bottom: 7px;
    font-size: 23px;
    color: var(--text-dark);
    white-space: nowrap;
  }
  .contact-icon {
    width: 32px;
    height: 32px;
    margin-right: 14px;
    flex: none;
  }
  .brand-lockup {
    position: absolute;
    left: 604px;
    top: 117px;
    height: 68px;
    display: flex;
    align-items: center;
  }
  .brand-dot {
    width: 68px;
    height: 68px;
    border-radius: 50%;
    background: var(--brand-orange);
    margin-right: 18px;
    flex: none;
  }
  .brand-name {
    font-family: "Montserrat", sans-serif;
    font-weight: 500;
    font-size: 40px;
    line-height: 1;
    color: var(--card-white);
    white-space: nowrap;
  }
</style>
</head>
<body>
  <div class="business-card">
    <svg class="card-panels" width="1116" height="302" viewBox="0 0 1116 302" aria-hidden="true">
      <polygon points="552,0 1116,0 1116,302 518,302" fill="var(--brand-orange)"/>
      <polygon points="560,0 1116,0 1116,302 526,302" fill="var(--card-black)"/>
    </svg>

    <div class="contact-side">
      <div class="holder-block">
        <p class="holder-name">Tecnologia &amp; Ciencias</p>
        <p class="holder-role">Cargo | Função</p>
      </div>
      <ul class="contact-list">
        <li class="contact-item">
          <svg class="contact-icon" viewBox="0 0 32 32" aria-hidden="true">
            <circle cx="16" cy="16" r="16" fill="var(--brand-orange)"/>
            <path d="M11 8.5c1-.6 2-.3 2.5.6l1.3 2.4c.4.8.2 1.6-.5 2.1l-1 .7c.8 1.8 2.2 3.3 4 4.2l.8-1c.5-.7 1.4-.8 2.1-.4l2.3 1.4c.9.5 1.1 1.6.5 2.5l-.8 1.1c-.7 1-2 1.4-3.1 1-4.600-1.6-8.1-5.2-9.5-9.8-.3-1.1.1-2.3 1-3z" fill="#fff"/>
          </svg>
          (00) 0000-0000
        </li>
        <li class="contact-item">
          <svg class="contact-icon" viewBox="0 0 32 32" aria-hidden="true">
            <circle cx="16" cy="16" r="16" fill="var(--brand-orange)"/>
            <rect x="8.5" y="10.5" width="15" height="11" rx="1.2" fill="#fff"/>
            <path d="M9 11.5l7 5.5 7-5.5" fill="none" stroke="var(--brand-orange)" stroke-width="1.4"/>
          </svg>
          contato@exemplo.com
        </li>
        <li class="contact-item">
          <svg class="contact-icon" viewBox="0 0 32 32" aria-hidden="true">
            <circle cx="16" cy="16" r="16" fill="var(--brand-orange)"/>
            <g fill="none" stroke="#fff" stroke-width="1.5">
              <circle cx="16" cy="16" r="7.5"/>
              <ellipse cx="16" cy="16" rx="3.2" ry="7.5"/>
              <line x1="8.5" y1="16" x2="23.5" y2="16"/>
            </g>
          </svg>
          www.exemplo.com.br
        </li>
      </ul>
    </div>

    <div class="brand-lockup">
      <div class="brand-dot" aria-hidden="true"></div>
      <p class="brand-name">Vértice &amp; Prisma</p>
    </div>
  </div>
</body>
</html>
```